Corvane Medical's new brochure MUST differentiate us from our competitors!

Corvane Medical Services is a medical equipment company specializing in providing enteral nutrition products & feeding pumps/devices to Medicaid children suffering from complicated gastric cases. Approximately 50% of these families are Spanish-speaking and our company employs almost all bilingual field and support staff to accommodate them. We get new clients through referrals from the clinicians (MD's & advanced practice nurses) that diagnose and treat these kids. Most other companies we compete with provide several other types of products and do not specialize in enteral feeding like we do. The brochure designs we want need to help us clearly illustrate our specialty to the clinicians that see these kids so they will choose us to refer them to. I am attaching a draft sketch I made up with copy and sample pics. We're open to any new logo designs as well!

Industry/Entity Type

Nutrition

```html
<!DOCTYPE html>
<html lang="en">
<head>
<meta charset="utf-8">
<title>Corvane Medical Services – Brochure Spread</title>
<link rel="stylesheet" href="https://fonts.googleapis.com/css2?family=Montserrat:wght@500;700&family=Open+Sans:wght@400;600&display=swap">
<style>
  :root {
    --brand-blue: #0d5a8c;
    --brand-blue-dark: #094670;
    --accent-orange: #f0a11e;
    --body-text: #555a5f;
    --page-white: #ffffff;
    --page-shade: #e6e7e9;
    --backdrop: #d9dadc;
    --gold-light: #f3d36b;
    --gold-dark: #b8860b;
  }
  * { box-sizing: border-box; margin: 0; padding: 0; }
  html, body { width: 1200px; height: 800px; overflow: hidden; }
  body { background: var(--backdrop); font-family: "Open Sans", Arial, sans-serif; }

  .spread {
    position: absolute; left: 60px; top: 50px;
    width: 1080px; height: 700px;
    display: flex;
    box-shadow: 0 6px 24px rgba(0,0,0,.18);
  }
  .page { position: relative; width: 540px; height: 700px; overflow: hidden; background: var(--page-white); }
  .page--left { background: linear-gradient(to right, #fff 70%, #eef0f2 100%); }
  .page--right { background: linear-gradient(to bottom, #fff 0%, #fff 30%, var(--page-shade) 60%); }

  .top-band { position: absolute; left: 0; top: 0; width: 540px; height: 70px; }

  .section-title {
    font-family: "Montserrat", Arial, sans-serif;
    font-weight: 700; font-size: 16px;
    color: var(--accent-orange);
    margin-bottom: 4px;
  }
  .section-copy { font-size: 13px; line-height: 1.38; color: var(--body-text); }
  .section + .section { margin-top: 16px; }

  /* Left page */
  .family-photo {
    position: absolute; left: 0; top: 52px; width: 205px; height: 390px;
    background: linear-gradient(160deg, #c9b45a 0%, #a8883c 35%, #d7843a 65%, #8a5a2e 100%);
  }
  .left-copy { position: absolute; left: 225px; top: 64px; width: 295px; }
  .contact-panel {
    position: absolute; left: 0; top: 442px; width: 262px; height: 258px;
    background: var(--brand-blue);
    padding: 58px 0 0 18px;
    color: #fff;
    font-family: "Montserrat", Arial, sans-serif; font-weight: 500; font-size: 15px;
    white-space: nowrap;
  }
  .contact-line { display: flex; align-items: center; gap: 9px; margin-bottom: 26px; }
  .contact-icon { width: 17px; height: 17px; flex: none; }
  .contact-at { width: 17px; text-align: center; font-weight: 700; }
  .program-graphic {
    position: absolute; left: 262px; top: 470px; width: 278px; height: 230px;
    background: radial-gradient(ellipse at 50% 35%, #9fd3f5 0%, #2b7fc4 40%, #0b3d7a 100%);
  }

  /* Right page */
  .right-copy { position: absolute; left: 36px; top: 74px; width: 396px; }
  .service-list { list-style: none; }
  .service-list li { position: relative; padding-left: 14px; font-size: 13px; line-height: 1.38; color: var(--body-text); }
  .service-list li::before {
    content: ""; position: absolute; left: 0; top: 6px;
    width: 7px; height: 7px; background: var(--brand-blue);
  }
  .quality-seal {
    position: absolute; left: 444px; top: 118px; width: 74px; height: 74px; border-radius: 50%;
    background: radial-gradient(circle at 40% 35%, var(--gold-light), var(--gold-dark));
    box-shadow: 0 2px 4px rgba(0,0,0,.25);
  }
  .family-scene { position: absolute; left: 0; top: 420px; width: 540px; height: 280px; }
</style>
</head>
<body>
  <main class="spread">
    <section class="page page--left">
      <svg class="top-band" viewBox="0 0 540 70" aria-hidden="true">
        <rect x="0" y="0" width="540" height="44" fill="var(--brand-blue)"/>
        <rect x="0" y="46" width="540" height="3" fill="var(--accent-orange)"/>
      </svg>

      <div class="family-photo" role="img" aria-label="Photo of a smiling mother and son holding autumn leaves"></div>

      <div class="left-copy">
        <div class="section">
          <h2 class="section-title">Specializing in nutrition.</h2>
          <p class="section-copy">Your patients came to you because of your specialization. Corvane Medical continues that specialized service by providing unique insight into the set-up, delivery and continued management of supplies &amp; equipment for nutritionally compromised children living at home. We supply more than just vital medical products to families, we provide peace of mind.</p>
        </div>
        <div class="section">
          <h2 class="section-title">Specializing in Medicaid.</h2>
          <p class="section-copy">Keeping up with the changes in state Medicaid programs is a critical component to optimizing outcomes for your patients. Corvane Medical has over 20 years of experience understanding the benefits, documentation and reimbursement requirements of Medicaid, state waiver programs and Managed Medicaid Replacement plans.</p>
        </div>
      </div>

      <div class="contact-panel">
        <div class="contact-line">
          <svg class="contact-icon" viewBox="0 0 24 24" aria-hidden="true"><path fill="#fff" d="M6.6 10.8a15 15 0 0 0 6.6 6.6l2.2-2.2c.3-.3.7-.4 1-.2 1.1.4 2.3.6 3.6.6.6 0 1 .4 1 1V20c0 .6-.4 1-1 1A17 17 0 0 1 3 4c0-.6.4-1 1-1h3.5c.6 0 1 .4 1 1 0 1.3.2 2.5.6 3.6.1.3 0 .7-.2 1z"/></svg>
          <span>(866) 555-0142</span>
        </div>
        <div class="contact-line">
          <svg class="contact-icon" viewBox="0 0 24 24" aria-hidden="true"><rect x="2" y="8" width="5" height="13" rx="1" fill="#fff"/><rect x="8" y="3" width="14" height="18" rx="1" fill="#fff"/><rect x="10" y="5" width="10" height="5" fill="var(--brand-blue)"/><rect x="10" y="12" width="2" height="2" fill="var(--brand-blue)"/><rect x="14" y="12" width="2" height="2" fill="var(--brand-blue)"/><rect x="18" y="12" width="2" height="2" fill="var(--brand-blue)"/><rect x="10" y="16" width="2" height="2" fill="var(--brand-blue)"/><rect x="14" y="16" width="2" height="2" fill="var(--brand-blue)"/><rect x="18" y="16" width="2" height="2" fill="var(--brand-blue)"/></svg>
          <span>(866) 555-0187</span>
        </div>
        <div class="contact-line">
          <span class="contact-at">@</span>
          <span>support@corvane247.com</span>
        </div>
      </div>

      <div class="program-graphic" role="img" aria-label="Blue digital illustration with winged medical emblem and the word Medicaid"></div>
    </section>

    <section class="page page--right">
      <svg class="top-band" viewBox="0 0 540 70" aria-hidden="true">
        <path d="M0 0 H540 V12 Q300 26 0 44 Z" fill="var(--brand-blue)"/>
        <path d="M0 47.5 Q300 29.5 540 15.5" fill="none" stroke="var(--accent-orange)" stroke-width="3"/>
      </svg>

      <div class="right-copy">
        <div class="section">
          <h2 class="section-title">Specializing in service.</h2>
          <ul class="service-list">
            <li>Bilingual field &amp; support staff for friendly, accurate communication.</li>
            <li>Easy patient referrals via fax, phone, web or secure email.</li>
            <li>Comprehensive, rapid supply set-ups and accurate home deliveries.</li>
            <li>Coordination of documentation paperwork to meet all regulatory requirements.</li>
            <li>Medicare, Medicaid, managed care &amp; most commercial insurances accepted.</li>
          </ul>
        </div>
        <div class="section">
          <h2 class="section-title">Specializing in quality.</h2>
          <p class="section-copy">Accreditation is an important component of quality care. Corvane Medical is accredited by the National Care Accreditation Council, the most recognized symbol of an organization's commitment to meet health care's highest quality performance standards.</p>
        </div>
      </div>

      <div class="quality-seal" aria-hidden="true"></div>

      <svg class="family-scene" viewBox="0 0 540 280" preserveAspectRatio="none" role="img" aria-label="Photo of a mother lying in a meadow lifting her baby into the air">
        <defs>
          <linearGradient id="meadow" x1="0" y1="0" x2="0" y2="1">
            <stop offset="0" stop-color="#dfe6e2"/>
            <stop offset="0.35" stop-color="#8fae6a"/>
            <stop offset="0.7" stop-color="#5f8a3a"/>
            <stop offset="1" stop-color="#3f6a2a"/>
          </linearGradient>
        </defs>
        <path d="M0 60 Q270 10 540 30 V280 H0 Z" fill="url(#meadow)"/>
      </svg>
    </section>
  </main>
</body>
</html>
```